Business cards and logo for Delcourt Law, P.A.

I need a business card and logo design for a new law firm in Miami, Florida called Delcourt Law, P.A. I, Theodore K. Delcourt, am the only lawyer in the firm. The law firm will mainly serve businesses but will also handle many other cases. Preferred colors are green and/or gray, but open minded to other suggestions.

Industry/Entity Type

Legal

Contact Information for Business Card

Phone Number TBD. Address is:
41 NE 3RD AVE STE 200
MIAMI, FL 33142

```html
<!DOCTYPE html>
<html lang="en">
<head>
<meta charset="utf-8">
<title>Delcourt Law, P.A. – Business Card</title>
<link rel="stylesheet" href="https://fonts.googleapis.com/css2?family=Cinzel:wght@400&family=Arimo:wght@400;700&display=swap">
<style>
  :root {
    --backdrop: #2a2a2c;
    --card-white: #f4f4f4;
    --card-white-edge: #e2e3e5;
    --navy: #0c2e5c;
    --brand-gray: #6f7276;
    --muted-gray: #8a8d91;
    --on-navy: #e9edf3;
  }
  * { box-sizing: border-box; margin: 0; padding: 0; }
  html, body { width: 1200px; height: 997px; overflow: hidden; }
  body {
    background: var(--backdrop);
    font-family: "Arimo", Arial, sans-serif;
    position: relative;
  }
  .business-card {
    position: absolute;
    left: 150px;
    top: 241px;
    width: 900px;
    height: 514px;
    border-radius: 26px;
    overflow: hidden;
    background: linear-gradient(180deg, #ffffff 0%, var(--card-white) 60%, var(--card-white-edge) 100%);
    box-shadow: 0 18px 40px rgba(0,0,0,0.55);
  }
  .brand {
    position: absolute;
    top: 92px;
    left: 232px;
    display: flex;
    align-items: center;
    gap: 22px;
  }
  .brand-square {
    width: 58px;
    height: 58px;
    background: var(--navy);
  }
  .brand-divider {
    width: 2px;
    height: 70px;
    background: var(--navy);
  }
  .brand-name {
    font-family: "Cinzel", "Times New Roman", serif;
    font-weight: 400;
    font-size: 50px;
    letter-spacing: 1px;
    color: var(--brand-gray);
  }
  .holder {
    position: absolute;
    top: 222px;
    left: 0;
    width: 100%;
    text-align: center;
  }
  .holder-name {
    font-weight: 700;
    font-size: 26px;
    letter-spacing: 0.5px;
    color: var(--navy);
  }
  .holder-title {
    font-size: 16px;
    letter-spacing: 1px;
    color: var(--muted-gray);
    margin-top: 2px;
  }
  .rule {
    position: absolute;
    left: 0;
    width: 100%;
    height: 4px;
    background: var(--navy);
  }
  .rule-upper { top: 292px; }
  .rule-lower { top: 304px; }
  .contact-band {
    position: absolute;
    left: 0;
    top: 316px;
    width: 100%;
    bottom: 0;
    background: var(--navy);
    color: var(--on-navy);
  }
  .website {
    position: absolute;
    right: 44px;
    top: 24px;
    font-size: 19px;
    letter-spacing: 0.3px;
  }
  .contact-list {
    list-style: none;
    position: absolute;
    left: 40px;
    top: 70px;
  }
  .contact-item {
    display: flex;
    align-items: center;
    gap: 14px;
    font-size: 19px;
    height: 38px;
  }
  .contact-icon { width: 22px; height: 22px; flex: none; }
</style>
</head>
<body>
  <div class="business-card">
    <div class="brand">
      <span class="brand-square"></span>
      <span class="brand-divider"></span>
      <span class="brand-name">Delcourt Law</span>
    </div>

    <div class="holder">
      <div class="holder-name">THEODORE K. DELCOURT</div>
      <div class="holder-title">ATTORNEY</div>
    </div>

    <div class="rule rule-upper"></div>
    <div class="rule rule-lower"></div>

    <div class="contact-band">
      <div class="website">www.delcourtlawpa.com</div>
      <ul class="contact-list">
        <li class="contact-item">
          <svg class="contact-icon" viewBox="0 0 22 22" aria-hidden="true">
            <circle cx="11" cy="11" r="11" fill="var(--on-navy)"/>
            <path d="M7.5 5.5l2 2.3-1.2 1.4c.8 1.6 2 2.8 3.6 3.6l1.4-1.2 2.3 2-1.3 1.7c-4.2-.4-7.9-4.1-8.3-8.3z" fill="var(--navy)"/>
          </svg>
          <span>+1 (305) 555-0148</span>
        </li>
        <li class="contact-item">
          <svg class="contact-icon" viewBox="0 0 22 22" aria-hidden="true">
            <circle cx="11" cy="11" r="11" fill="var(--on-navy)"/>
            <rect x="5.5" y="7" width="11" height="8" rx="1" fill="var(--navy)"/>
            <path d="M6 7.6l5 4 5-4" fill="none" stroke="var(--on-navy)" stroke-width="1.1"/>
          </svg>
          <span>office@dlkfirm.com</span>
        </li>
        <li class="contact-item">
          <svg class="contact-icon" viewBox="0 0 22 22" aria-hidden="true">
            <circle cx="11" cy="11" r="11" fill="var(--on-navy)"/>
            <path d="M11 4.5a4 4 0 0 0-4 4c0 3 4 8 4 8s4-5 4-8a4 4 0 0 0-4-4z" fill="var(--navy)"/>
            <circle cx="11" cy="8.6" r="1.5" fill="var(--on-navy)"/>
          </svg>
          <span>41 NE 3rd Ave, FL 33142</span>
        </li>
      </ul>
    </div>
  </div>
</body>
</html>
```